Project Willow Crest; Retail packaging for handmade bar soap.

A clean design that conveys quality and affordable luxury. Wrapper material is 80 lb felt cover paper, used as a wrap around the product.

Attached is my idea. Logo is purchased. Unless you think it's terrible, maybe best is to refine what I have? I'm thinking fonts, proportions, etc. Honestly though, if you think it's bad we can start from scratch. I think it's good but I'm not that invested in it. I just want to sell good soap.
5 different fragrances, each identical packaging except the colored stripe and the scent name. Should the scent name be inside the colored stripe or above it?

Apologies for the non-metric:
Soap is 3" tall and 2-13/16" wide and 1" deep.
Front of label is 2-5/16" tall and 2-13/16" wide.
Label (wrap) is 8-1/2" long

Looking forward to hearing from you guys.

Target Market(s)

retail gift shops, health food stores, hotel gift shops.

Industry/Entity Type

retail and online personal care products

Other font styles liked:
• not decorative or script

Colors
0054AA
0677BA
7BADD7
CADEEF
E8F1F8
59FF00
82FF00
B8FF75
E3FFCB
F4FFEA
FFF300
FFF600
FEFA6F
FFFEC7
FFFEE8
EB3D1F
EC4F4E
F09395
F8D3D4
FCEDEE
A7469A
B969AE
D3A5CF
EDDBEB
F8F0F9

Requirements
Must have
• The best word I can think of is feng shui. My soap makes you feel good when you use it. It's simple and clean. I want the same in the label.

```html
<!DOCTYPE html>
<html lang="en">
<head>
<meta charset="utf-8">
<title>Willow Crest Soap Co. – Coconut and Lemongrass Wrap</title>
<link rel="stylesheet" href="https://fonts.googleapis.com/css2?family=Montserrat:wght@400;500;600;700&display=swap">
<style>
  :root {
    --backdrop: #e3e3e3;
    --paper: #fbfbfa;
    --ink: #3b3b3b;
    --scent-green: #7c9f5a;
    --grass-light: #e4ecd2;
    --grass-mid: #c9d9a8;
    --rule: #3b3b3b;
  }
  * { box-sizing: border-box; margin: 0; padding: 0; }
  html, body {
    width: 750px;
    height: 1200px;
    overflow: hidden;
    background: var(--backdrop);
    font-family: "Montserrat", sans-serif;
    color: var(--ink);
  }
  .canvas {
    width: 750px;
    height: 1200px;
    display: flex;
    flex-direction: column;
  }
  .panel-slot {
    height: 600px;
    display: flex;
    align-items: center;
    justify-content: center;
  }
  .panel-slot + .panel-slot { border-top: 1px solid #d4d4d4; }
  .wrap-panel {
    position: relative;
    width: 380px;
    height: 372px;
    background: var(--paper);
    box-shadow: 0 1px 3px rgba(0,0,0,0.08);
    overflow: hidden;
  }
  .grass-pattern {
    position: absolute;
    top: 0;
    bottom: 0;
    width: 92px;
  }
  .grass-pattern--left {
    left: 0;
    background: linear-gradient(90deg, var(--grass-mid) 0%, var(--grass-light) 45%, rgba(251,251,250,0) 100%);
  }
  .grass-pattern--right {
    right: 0;
    background: linear-gradient(270deg, var(--grass-mid) 0%, var(--grass-light) 45%, rgba(251,251,250,0) 100%);
  }
  .panel-content {
    position: relative;
    height: 100%;
    display: flex;
    flex-direction: column;
    align-items: center;
    text-align: center;
    padding: 0 54px;
  }

  /* front */
  .front .panel-content { padding-top: 78px; }
  .brand-name {
    font-size: 16px;
    font-weight: 600;
    letter-spacing: 0.2px;
  }
  .brand-mark {
    margin: 26px 0 24px;
    display: flex;
    align-items: center;
    gap: 8px;
    font-size: 15px;
    font-weight: 500;
    height: 92px;
  }
  .brand-mark .dot {
    width: 10px;
    height: 10px;
    border-radius: 50%;
    background: var(--ink);
  }
  .tagline {
    font-size: 11px;
    font-weight: 400;
    line-height: 1.15;
  }
  .divider {
    width: 38px;
    height: 1px;
    background: var(--rule);
    margin: 7px 0 10px;
  }
  .scent-name {
    font-size: 24px;
    font-weight: 600;
    line-height: 1.12;
    color: var(--scent-green);
  }

  /* back */
  .back .panel-content { padding-top: 66px; padding-left: 40px; padding-right: 40px; }
  .section-title {
    font-size: 16px;
    font-weight: 400;
    margin-bottom: 5px;
  }
  .section-text {
    font-size: 11px;
    line-height: 1.28;
    margin-bottom: 14px;
  }
  .web-address {
    font-size: 15px;
    font-weight: 400;
    margin-top: 12px;
    margin-bottom: 20px;
  }
  .slogan {
    font-size: 14px;
    font-weight: 600;
    line-height: 1.35;
  }
</style>
</head>
<body>
<main class="canvas">

  <section class="panel-slot">
    <article class="wrap-panel front">
      <div class="grass-pattern grass-pattern--left" role="img" aria-label="Pale green lemongrass stalk pattern"></div>
      <div class="grass-pattern grass-pattern--right" role="img" aria-label="Pale green lemongrass stalk pattern"></div>
      <div class="panel-content">
        <h1 class="brand-name">Willow Crest Soap Co.</h1>
        <div class="brand-mark"><span class="dot"></span><span>Willow Crest</span></div>
        <p class="tagline">All-Natural and Handmade<br>on the Coast</p>
        <div class="divider"></div>
        <h2 class="scent-name">Coconut and<br>Lemongrass</h2>
      </div>
    </article>
  </section>

  <section class="panel-slot">
    <article class="wrap-panel back">
      <div class="grass-pattern grass-pattern--left" role="img" aria-label="Pale green lemongrass stalk pattern"></div>
      <div class="grass-pattern grass-pattern--right" role="img" aria-label="Pale green lemongrass stalk pattern"></div>
      <div class="panel-content">
        <h3 class="section-title">Ingredients</h3>
        <p class="section-text">Saponified Oils: (Coconut, Olive, Sustainable Certified Palm, Cocoa Butter and Castor oil)</p>
        <h3 class="section-title">Goodies</h3>
        <p class="section-text">glycerin, artesian spring water, white porcelain clay, Oregon honey, fermentation derived natural citric acid and lactic acid, Oregon sea salt, natural fragrances and natural earth colorants</p>
        <p class="web-address">WillowCrestSoap.us</p>
        <p class="slogan">Buy good coffee?<br>Buy good soap!</p>
      </div>
    </article>
  </section>

</main>
</body>
</html>
```